Business card design needed

Our company background is that we provides transfers to and from the airport, social & corporate events, weddings.
We are also available for charter for birthday party, wine tastings, concerts, anniversary, school balls etc.
Our business cards have to reflect that we have a professional company, they are our first contact and have to stand out from the other 'players' in the market.

Industry/Entity Type

School

Contact Information for Business Card

BRISTEL QDF, Laurent & Marisol, mob: 0427 381 594, PO Box 287, Tarrowin WA 6311, ABN 52 914 603 278, Lic 7169/5804,

Requirements
Must have
• Telephone number: 0427 381 594
Website: www.BRISTELQDF.com.au
postal address: PO Box 287, Tarrowin WA 6311
Licences: Lic 7169/5804

***If using the new photo (one with the bus and buildings behind it), if possible can the buildings be cropped out. Thanks
Nice to have
• would be nice to have the pics of the vehicle(s), preferred the Pel on the card but not too fussed.
Should not have
• Picture of vehicle we don't have in our fleet. (We ONLY have the Pellics and Rendak Ovaro mini bus)

```html
<!DOCTYPE html>
<html lang="en">
<head>
<meta charset="utf-8">
<title>BRISTEL QDF – Business Card</title>
<link rel="stylesheet" href="https://fonts.googleapis.com/css2?family=Open+Sans:wght@300;400&display=swap">
<style>
  :root {
    --card-black: #000000;
    --panel-light: #3b3e40;
    --panel-dark: #0e0f10;
    --footer-band: #070707;
    --text-white: #f4f4f4;
    --vehicle-light: #eef0f1;
    --vehicle-shade: #b9bec2;
  }
  html, body {
    margin: 0;
    padding: 0;
    width: 1200px;
    height: 741px;
    overflow: hidden;
    background: var(--card-black);
  }
  .card {
    position: relative;
    width: 1200px;
    height: 741px;
    background: var(--card-black);
    font-family: "Open Sans", Arial, sans-serif;
    color: var(--text-white);
    overflow: hidden;
  }
  .contact-panel {
    position: absolute;
    left: 0;
    top: 0;
    width: 430px;
    height: 692px;
    background: radial-gradient(ellipse 120% 90% at 0% 45%, var(--panel-light) 0%, #222425 45%, var(--panel-dark) 100%);
  }
  .footer-band {
    position: absolute;
    left: 0;
    bottom: 0;
    width: 1200px;
    height: 49px;
    background: var(--footer-band);
  }
  .brand-name {
    position: absolute;
    right: 44px;
    top: 78px;
    margin: 0;
    font-weight: 300;
    font-size: 58px;
    letter-spacing: 3px;
    line-height: 1;
    color: var(--text-white);
    white-space: nowrap;
  }
  .owners {
    position: absolute;
    left: 48px;
    top: 282px;
    margin: 0;
    font-weight: 400;
    font-size: 32px;
    letter-spacing: 1px;
    text-shadow: 0 2px 4px rgba(0,0,0,0.6);
  }
  .owners-rule {
    position: absolute;
    left: 48px;
    top: 342px;
    width: 335px;
    height: 2px;
    background: var(--text-white);
  }
  .contact-list {
    position: absolute;
    left: 48px;
    top: 0;
    margin: 0;
    padding: 0;
    list-style: none;
    font-size: 20px;
    font-weight: 400;
    letter-spacing: 0.3px;
  }
  .contact-list li {
    position: absolute;
    left: 0;
    white-space: nowrap;
    text-shadow: 0 2px 3px rgba(0,0,0,0.6);
  }
  .contact-mobile { top: 385px; }
  .contact-address { top: 434px; }
  .contact-abn { top: 491px; }
  .contact-licence { top: 540px; }
  .contact-web { top: 589px; }
  .vehicle-photo {
    position: absolute;
    left: 592px;
    top: 290px;
    width: 538px;
    height: 364px;
  }
</style>
</head>
<body>
  <div class="card">
    <div class="contact-panel"></div>
    <div class="footer-band"></div>

    <h1 class="brand-name">BRISTEL QDF</h1>

    <h2 class="owners">LAURENT &amp; MARISOL</h2>
    <div class="owners-rule"></div>

    <ul class="contact-list">
      <li class="contact-mobile">Mobile : 0427 381 594</li>
      <li class="contact-address">PO Box 287, Tarrowin WA 6311</li>
      <li class="contact-abn">ABN 52 914 603 278</li>
      <li class="contact-licence">Lic 7169/5804</li>
      <li class="contact-web">www.BRISTELQDF.com.au</li>
    </ul>

    <svg class="vehicle-photo" viewBox="0 0 538 364" role="img" aria-label="Photo of the white Rendak Ovaro mini bus, front three-quarter view">
      <defs>
        <linearGradient id="vehicleTone" x1="0" y1="0" x2="1" y2="1">
          <stop offset="0" stop-color="var(--vehicle-light)"/>
          <stop offset="1" stop-color="var(--vehicle-shade)"/>
        </linearGradient>
      </defs>
      <rect x="0" y="0" width="538" height="364" rx="28" fill="url(#vehicleTone)"/>
    </svg>
  </div>
</body>
</html>
```